Concise,Good colour matching,Good looks design for "HERD SURE RAPID TEST FOR LIVESTOCK"

Product Positioning: Affordable test for Large Animals (Livestock/Veterinary Use)
Product Name: HERD SURE Rapid Test Kit (for large animals, e.g., cattle, horses, swine,Avian,sheep).

2. Packaging Requirements

A. Visual Design
Color Scheme:
Green/Blue/Orange/Yellow/Red/Gray/White(chose 2~4 colors)

Mandatory Info:
Brand logo ("HERD SURE")

Target Market(s)

Southeast Asia, Africa, Middle East, South America

Industry/Entity Type

Veterinary diagnostic for LIVESTOCK

Colors

Designer to choose colors to be used in the design.

Requirements
Nice to have
• Concise,Good colour matching,Good looks

```html
<!DOCTYPE html>
<html lang="en">
<head>
<meta charset="utf-8">
<title>HERD SURE Rapid Test – Box Dieline</title>
<link href="https://fonts.googleapis.com/css2?family=Montserrat:wght@400;500;700;800&family=Open+Sans:wght@400&display=swap" rel="stylesheet">
<style>
  :root {
    --brand-red: #ff3d00;
    --brand-amber: #ff9e00;
    --label-yellow: #fce07a;
    --label-pale: #fbecb8;
    --dieline: #d6195b;
    --fold: #9a8f8f;
    --paper: #ffffff;
    --ink: #222222;
    --measure: #333333;
  }
  html, body {
    margin: 0;
    padding: 0;
    width: 1200px;
    height: 1200px;
    overflow: hidden;
    background: var(--paper);
  }
  .dieline-sheet { display: block; width: 1200px; height: 1200px; }
  .font-brand { font-family: "Montserrat", sans-serif; }
  .font-measure { font-family: "Open Sans", sans-serif; }
  .cut { fill: none; stroke: var(--dieline); stroke-width: 1.3; }
  .fold { stroke: var(--fold); stroke-width: 0.7; fill: none; }
  .fill-red { fill: var(--brand-red); }
  .fill-amber { fill: var(--brand-amber); }
  .fill-white { fill: var(--paper); }
  .fill-yellow { fill: var(--label-yellow); }
  .fill-pale { fill: var(--label-pale); }
  .wordmark { font-family: "Montserrat", sans-serif; font-weight: 800; letter-spacing: 0.5px; }
  .tagline { font-family: "Montserrat", sans-serif; font-weight: 700; }
  .body-copy { font-family: "Montserrat", sans-serif; font-weight: 400; }
  .body-strong { font-family: "Montserrat", sans-serif; font-weight: 700; }
  .dimension-line { stroke: var(--measure); stroke-width: 1; }
  .dimension-label { font-family: "Open Sans", sans-serif; fill: var(--ink); }
</style>
</head>
<body>
<svg class="dieline-sheet" viewBox="0 0 1200 1200" xmlns="http://www.w3.org/2000/svg">
  <defs>
    <marker id="arrow-head" viewBox="0 0 10 10" refX="9" refY="5" markerWidth="7" markerHeight="7" orient="auto-start-reverse">
      <path d="M0 0 L10 5 L0 10 z" fill="#333333"/>
    </marker>
    <linearGradient id="herd-photo-tone" x1="0" y1="0" x2="1" y2="1">
      <stop offset="0" stop-color="#c9a35a"/>
      <stop offset="0.5" stop-color="#a9823f"/>
      <stop offset="1" stop-color="#8c6a33"/>
    </linearGradient>
  </defs>

  <!-- Box size note -->
  <text class="dimension-label" x="270" y="49" font-size="6">150×110×80 (mm)</text>

  <!-- Top dust flaps -->
  <g class="dust-flaps">
    <path class="fill-red" d="M311 75 L511 75 L549 203 L549 214 L294 214 L300 206 Z"/>
    <path class="cut" d="M311 75 L511 75 L549 203 L549 214 M294 214 L300 206 L311 75"/>
    <path class="fill-red" d="M938 75 L1136 75 L1149 206 L1155 214 L899 214 L899 203 Z"/>
    <path class="cut" d="M899 203 L938 75 L1136 75 L1149 206 L1155 214"/>
  </g>

  <!-- Left side panel -->
  <g class="side-panel side-panel--left">
    <path class="cut" d="M294 219 L270 219 L270 396 L294 400"/>
    <rect class="fill-red" x="294" y="214" width="255" height="186"/>
    <path class="cut" d="M294 400 L294 424 L546 424 L549 400"/>
    <text class="body-strong fill-amber" x="303" y="254" font-size="12.5" letter-spacing="0.5">RAPID TEST</text>
    <text class="wordmark fill-white" x="542" y="255" font-size="20" text-anchor="end">HERD SURE</text>

    <g class="benefit-list" font-size="5.8" fill="#ffffff">
      <text x="305" y="309"><tspan class="body-strong">Fast &amp; Efficient:</tspan><tspan class="body-copy"> Rapid test results in less than</tspan></text>
      <text class="body-copy" x="305" y="317">10 minutes from prep to completion</text>
      <text x="305" y="331"><tspan class="body-strong">Affordable:</tspan><tspan class="body-copy"> Colloidal gold-based rapid tests</tspan></text>
      <text class="body-copy" x="305" y="339">that combine high accuracy</text>
      <text class="body-copy" x="305" y="347">with cost-effectiveness.</text>
      <text x="305" y="361"><tspan class="body-strong">Reliable &amp; Simple:</tspan><tspan class="body-copy"> Stable test performance</tspan></text>
      <text class="body-copy" x="305" y="369">with 2-30 °C. Easy to operate, no professional</text>
      <text class="body-copy" x="305" y="377">skills required.</text>
    </g>
    <rect class="brand-block fill-amber" x="462" y="300" width="78" height="78"/>
  </g>

  <!-- Top (lid) panel -->
  <g class="panel panel--lid">
    <rect class="fill-red" x="549" y="214" width="350" height="186"/>
    <path d="M711 214 A14 14 0 0 0 739 214" class="cut" fill="#ff3d00"/>
    <text class="wordmark fill-white" x="724" y="305" font-size="28" text-anchor="middle">HERD SURE</text>
    <text class="tagline fill-amber" x="724" y="326" font-size="12.5" text-anchor="middle">Affordable Diagnostics</text>
    <text class="tagline fill-amber" x="724" y="339" font-size="12.5" text-anchor="middle">for Healthy Herds</text>
  </g>

  <!-- Right side panel -->
  <g class="side-panel side-panel--right">
    <rect class="fill-white" x="899" y="214" width="256" height="186"/>
    <path class="cut" d="M1155 219 L1179 219 L1179 396 L1155 400"/>
    <path class="cut" d="M902 400 L902 424 L1155 424 L1155 400"/>
    <rect class="fill-yellow" x="917" y="236" width="111" height="130"/>
    <rect class="fill-pale" x="923" y="272" width="52" height="52" opacity="0.8"/>
    <text class="body-strong" x="925" y="247" font-size="6.2" fill="#333">AVIAN ENCEPHALOMYELITIS</text>
    <text class="body-copy" x="925" y="255" font-size="6" fill="#555">VIRUS ANTIBODY TEST KIT</text>
    <rect class="fill-amber" x="917" y="371" width="111" height="17"/>
    <text class="wordmark fill-white" x="923" y="384" font-size="10">HERD SURE</text>

    <g class="body-copy" font-size="6.3" fill="#333" text-anchor="middle">
      <text x="1087" y="247">AE Ab Test is an enzyme-linked</text>
      <text x="1087" y="255">immunosorbent assay (ELISA)</text>
      <text x="1087" y="263">designed to detect antibody to</text>
      <text x="1087" y="271">avian encephalomyelitis viruses</text>
      <text x="1087" y="279">(AE) in chicken serum.</text>
    </g>
    <g class="body-copy" font-size="4.6" fill="#333" text-anchor="middle">
      <text x="1087" y="300">Store kit components at stated</text>
      <text x="1087" y="306">temperature. Bring reagents to room</text>
      <text x="1087" y="312">temperature before use. Read all</text>
      <text x="1087" y="318">steps fully prior to testing.</text>
      <text x="1087" y="324">For veterinary use only.</text>
      <text x="1087" y="330">Results should be read by</text>
      <text x="1087" y="336">trained staff.</text>
    </g>
    <g font-size="5.4" fill="#222" text-anchor="middle">
      <text class="body-strong" x="1087" y="374">Manufactured by HERDLAB</text>
      <text class="body-copy" x="1087" y="381">Storage: 2-30 °C, Do not freeze</text>
      <text class="body-copy" x="1087" y="388">See the instructions for other contents</text>
    </g>
  </g>

  <!-- Back panel (110mm) -->
  <g class="panel panel--back">
    <rect class="fill-red" x="549" y="400" width="350" height="256"/>
    <rect class="brand-block fill-amber" x="590" y="430" width="120" height="120"/>
    <text class="wordmark fill-white" x="714" y="531" font-size="22">HERD SURE</text>
    <text class="tagline fill-white" x="712" y="545" font-size="13.5">Affordable Diagnostics</text>
    <text class="tagline fill-white" x="712" y="559" font-size="13.5">for Healthy Herds</text>
  </g>

  <!-- Base panel (80mm), printed inverted -->
  <g class="panel panel--base">
    <rect class="fill-red" x="549" y="656" width="350" height="188"/>
    <g transform="rotate(180 724 720)">
      <text class="wordmark fill-amber" x="724" y="699" font-size="25" text-anchor="middle">HERD SURE</text>
      <g class="body-copy fill-white" font-size="9.5" text-anchor="middle">
        <text x="724" y="732">Manufactured by HERDLAB</text>
        <text x="724" y="744">Storage: 2-30 °C, Do not freeze</text>
        <text x="724" y="756">See the instructions for other contents</text>
      </g>
    </g>
  </g>

  <!-- Front panel -->
  <g class="panel panel--front">
    <rect class="fill-white" x="549" y="844" width="350" height="254"/>
    <rect x="551" y="853" width="348" height="170" fill="url(#herd-photo-tone)" role="img" aria-label="Sepia photo grid of livestock: horse, cow, rooster, pig, duck and sheep"/>
    <rect class="fill-red" x="551" y="1023" width="348" height="38"/>
    <text class="tagline fill-white" x="568" y="1040" font-size="12.5">Affordable Diagnostics</text>
    <text class="tagline fill-white" x="568" y="1053" font-size="12.5">for Healthy Herds</text>
    <text class="wordmark fill-red" x="872" y="1084" font-size="21" text-anchor="end">HERD SURE</text>
    <path class="cut" d="M551 1098 L551 1112 Q551 1132 571 1132 L877 1132 Q897 1132 897 1112 L897 1098"/>
  </g>

  <!-- Folds and outer cuts -->
  <g class="folds">
    <line class="fold" x1="549" y1="400" x2="899" y2="400"/>
    <line class="fold" x1="549" y1="656" x2="899" y2="656"/>
    <line class="fold" x1="294" y1="400" x2="549" y2="400"/>
    <line class="fold" x1="899" y1="400" x2="1155" y2="400"/>
    <line class="fold" x1="551" y1="1098" x2="897" y2="1098"/>
  </g>
  <path class="cut" d="M549 400 L549 1098 M899 400 L899 1098"/>

  <!-- Dimensions -->
  <g class="dimensions">
    <line class="dimension-line" x1="552" y1="188" x2="896" y2="188" marker-start="url(#arrow-head)" marker-end="url(#arrow-head)"/>
    <text class="dimension-label" x="720" y="181" font-size="23" text-anchor="middle">150mm</text>
    <line class="dimension-line" x1="958" y1="406" x2="958" y2="654" marker-start="url(#arrow-head)" marker-end="url(#arrow-head)"/>
    <text class="dimension-label" font-size="23" text-anchor="middle" transform="translate(970 530) rotate(90)">110mm</text>
    <line class="dimension-line" x1="958" y1="659" x2="958" y2="828" marker-start="url(#arrow-head)" marker-end="url(#arrow-head)"/>
    <text class="dimension-label" font-size="23" text-anchor="middle" transform="translate(970 735) rotate(90)">80mm</text>
  </g>
</svg>
</body>
</html>
```